Web design for new streaming audio service

We need a homepage design for a new streaming audio service. Our company is called Olvantra, and we’re basically Vidorama for Audiobooks, Stand-Up Comedy, Lectures, Language Learning, etc. Essentially like Tunelark for everything audio EXCEPT music.
You don’t have to code the homepage (Design Only), but it should include 3 different designs to work with 1) Web; 2) Phones; 3) Tablets.
Below is a link to a mockup of the web version which gives a good idea of what elements we want. This is just a mockup and we want you to improve it.
Once you download the mockup, please refer to the more detailed instructions below:
The following outlines the design project for the Olvantra homepage. We have provided a rough mockup of the homepage layout that gives you a general idea of what we’re going for. There are a few elements that we are attached to, and many others where you have complete creative freedom to do whatever you think looks good.
The ZIP file includes the following:
* Mockup to see what we have in mind (olvantra-homepage-mockup.jpg)
* Text used (olvantra-homepage-text.txt)
* Raw image of actor (olvantra-actor1.jpg)
* Raw images for samples (olvantra-sample-[name].jpg)
Although we have only provided a mockup layout for the web version, we also need you to provide a mobile phone and a tablet version of the design also. It’s very possible the tablet version may be substantially similar to the web version, but the mobile phone version will likely be much different.
All of the raw files are included in the attached ZIP file. Please use our photographs and text as provided although cropping, sizing, etc. is flexible per the instructions below.
Display Requirements:
* Web Version - Minimum resolution 1024x768 (72 dpi) but should look good on 1920x1080 (72 dpi) - Page should be designed to scale to look acceptable in all resolutions in between.
* Phone Version - Minimum Zentro 4 - 640x960 (326 dpi) but should look good on Korvel Nimbus Q5 - 1920x1080 (441 dpi) - Page should be designed to scale to look acceptable in all resolutions and devices in between.
* Tablet Version - Minimum Pagewick Ember LX 7” - 1280x800 (216 dpi) but should also look good on a Slato Breeze - 2048x1536 (264 dpi) - Page should be designed to scale to look acceptable in all resolutions and devices in between.
Above the Fold - We want to make sure the Olvantra logo, Member Login Link, Large Photo, Headline, Price, Button, and the first row of sample images are all “Above the fold”. As a general guideline, this means 600 pixels high on a 1024x768 72 dpi web screen. This requirement is less important on Phone versions.
Top Logo Bar - We want to retain the blue bar with the Olvantra logo on the page, although we are open to a different size, shape and positioning if it greatly enhances the design. Please use the standard logo color, although you are welcome to use either the horizontal or vertical orientation of the logo based on your design.
Text color, font and size - Feel free to design the text in anyway you choose as long as the text is readable on the target platforms.
Buttons - Feel free to use any size, shape and colors for the buttons as long as they are obvious and clickable relative to the page. The only exception is the Chatterly button should follow the Chatterly color scheme and logo treatment (the mockup doesn’t seem 100% correct.)
Top Photograph - We want to retain the large photograph across the top of the screen although final shape and dimensions are flexible.
Size and shape of content samples (i.e. Audiobooks, Stand-Up Comedy, etc.) - Feel free to design the content samples in anyway you choose.
Three Sales Points (i.e. Listen on your Zentro…, All you can enjoy…, etc.) - The Three Sales Points are envisioned to each have a corresponding illustration which you should provide and have rights for. The placeholder is represented by a square next to the text. The color size and shape of these elements are flexible and can be designed in any way you choose.
Opt-in form - Feel free to design the opt-in form in anyway you choose as long as the text is readable and the interactivity is obvious on the target platforms.
Text links and copyright notice - Feel free to design the bottom of the page text links and copyright notice in anyway you choose.
Additional colors, graphic design elements, etc. - Feel free to use any additional colors, graphic design elements, etc. to support your design.

```html
<!DOCTYPE html>
<html lang="en">
<head>
<meta charset="utf-8">
<title>Olvantra – Unlimited Listening</title>
<link href="https://fonts.googleapis.com/css2?family=Asap:wght@400;500;600;700&display=swap" rel="stylesheet">
<style>
:root{
  --blue:#3b8fc4;
  --blue-dark:#2f7fb3;
  --blue-text:#4a6f95;
  --link:#3f9fd8;
  --green:#5ec56e;
  --grey-btn:#9a9a9a;
  --ink:#333;
  --muted:#666;
  --page:#f3f3f3;
  --card:#fbfbfb;
  --rule:#e4e4e4;
  --chatterly:#5d6fb8;
  --chatterly-dark:#4a5a9e;
  --dark:#3a3a3a;
}
*{margin:0;padding:0;box-sizing:border-box}
html,body{width:889px;height:1200px;overflow:hidden}
body{background:var(--page);font-family:"Asap",sans-serif;color:var(--ink);position:relative}
.abs{position:absolute}

.topbar{left:0;top:0;width:889px;height:44px;background:linear-gradient(#4aa0d2,var(--blue-dark))}
.brand{left:74px;top:9px;display:flex;align-items:center;gap:7px;color:#fff;font-size:20px;font-weight:600}
.brand-dot{width:22px;height:22px;border-radius:50%;background:#fff;opacity:.9}
.login{left:692px;top:8px;width:123px;height:28px;background:#2e7bae;border:1px solid #2a6f9e;border-radius:2px;color:#fff;font-size:13px;display:flex;align-items:center}
.login-lock{width:28px;display:flex;justify-content:center}
.login span{padding-left:8px}

.hero{left:0;top:44px;width:889px;height:292px;background:#fff;overflow:hidden}
.hero-photo{position:absolute;left:360px;top:0;width:529px;height:292px;
  background:radial-gradient(ellipse at 55% 45%,#d9b59a 0%,#c99f86 28%,#b9c7d6 55%,rgba(255,255,255,0) 78%),
             linear-gradient(90deg,#fff 0%,rgba(255,255,255,0) 30%),
             linear-gradient(#e9eef3,#c9d6e2)}
.headline{left:74px;top:80px;width:320px;text-align:center;color:var(--blue-text);font-size:37px;line-height:44px;font-weight:400;letter-spacing:-.5px}
.price{left:74px;top:165px;width:320px;text-align:center;color:var(--blue-dark);font-size:19px}
.price .cur{font-size:15px;vertical-align:22px}
.price .big{font-size:42px;font-weight:500}
.price .cents{font-size:24px}
.cta{left:106px;top:220px;width:246px;height:38px;background:var(--green);color:#fff;font-size:22px;font-weight:500;display:flex;align-items:center;justify-content:center}
.cta-note{left:106px;top:262px;width:246px;text-align:center;font-size:11px;color:var(--blue-text)}

.section-title{left:75px;top:351px;font-size:20px;color:var(--blue-dark);font-weight:500}
.dots{left:759px;top:362px;display:flex;gap:7px}
.dots i{width:9px;height:9px;border-radius:50%;background:#c8c8c8;display:block}
.dots i:first-child{background:var(--link)}
.rule{left:75px;width:740px;height:1px;background:var(--rule)}

.sample{top:403px;width:170px;text-align:center}
.sample-art{width:170px;height:170px;border-radius:50%}
.sample h3{margin-top:14px;font-size:16px;font-weight:600;color:var(--dark)}
.sample p{margin-top:6px;font-size:12px;line-height:18px;color:var(--muted)}
.sample .btn{margin:12px auto 0;width:102px;height:28px;background:var(--grey-btn);color:#fff;font-size:10px;font-weight:700;display:flex;align-items:center;justify-content:center}
.sample.active h3{color:var(--link)}
.sample.active p{color:var(--ink)}
.sample.active .btn{background:var(--link)}

.feature{top:736px;height:232px;background:var(--card);box-shadow:0 1px 2px rgba(0,0,0,.12)}
.feature-art{position:absolute;left:50%;top:32px;width:124px;height:128px;margin-left:-62px;border-radius:6px;
  background:radial-gradient(circle at 50% 45%,#cfe3f2 0%,#e6e9ec 60%,#eeeeee 100%)}
.feature p{position:absolute;left:0;right:0;top:181px;text-align:center;font-size:14px;line-height:16px;color:var(--ink)}
.feature b{font-weight:400;color:var(--link)}

.signup{left:75px;top:1021px;width:369px;height:112px;background:var(--green)}
.signup h2{position:absolute;left:12px;top:8px;color:#fff;font-size:18px;font-weight:600}
.email{position:absolute;left:11px;top:35px;width:256px;height:27px;background:#fff;border:1px solid #ccc;font-size:12px;color:#888;display:flex;align-items:center;padding-left:8px;gap:8px}
.signup-btn{position:absolute;left:276px;top:35px;width:84px;height:27px;background:#333;color:#fff;font-size:10px;font-weight:700;display:flex;align-items:center;justify-content:center}
.signup-note{position:absolute;left:0;bottom:0;width:369px;height:37px;background:#3c3c3c;color:#fff;font-size:8.5px;line-height:12px;padding:6px 7px}
.signup-note em{font-style:normal;color:var(--link)}
.signup-note .g{color:var(--green)}
.signup-note .soft{color:#bbb}

.access{left:470px;top:1021px;width:344px;height:41px;background:var(--grey-btn);color:#fff;font-size:15px;font-weight:600;display:flex;align-items:center}
.access .side,.social .side{width:42px;height:100%;display:flex;align-items:center;justify-content:center;background:rgba(0,0,0,.18)}
.access span,.social span{flex:1;text-align:center}
.or{left:470px;top:1070px;width:344px;text-align:center;font-size:12px;font-weight:700;color:var(--dark)}
.social{left:470px;top:1092px;width:344px;height:41px;background:var(--chatterly);color:#fff;font-size:15px;font-weight:600;display:flex;align-items:center}
.social .side{background:var(--chatterly-dark)}

.copyright{left:75px;top:1171px;font-size:10px;color:var(--dark)}
.footer-links{right:74px;top:1171px;font-size:10px;color:#777}
</style>
</head>
<body>

<header class="abs topbar"></header>
<div class="abs brand"><i class="brand-dot"></i>Olvantra</div>
<div class="abs login">
  <div class="login-lock"><svg width="10" height="12" viewBox="0 0 10 12"><rect x="0" y="5" width="10" height="7" fill="#fff"/><path d="M2 5V3.5a3 3 0 0 1 6 0V5" stroke="#fff" stroke-width="1.6" fill="none"/></svg></div>
  <span>Member Login</span>
</div>

<section class="abs hero">
  <div class="hero-photo" role="img" aria-label="Smiling young man wearing headphones, listening on his phone"></div>
</section>
<h1 class="abs headline">Unlimited Listening.<br>Wherever you are.</h1>
<div class="abs price">Only <span class="cur">$</span><span class="big">9</span><span class="cents">.99</span> per month</div>
<div class="abs cta">Start Your Free Trial</div>
<div class="abs cta-note">* Credit Card Not Required</div>

<h2 class="abs section-title">A sample of what you can listen to on Olvantra</h2>
<div class="abs dots"><i></i><i></i><i></i><i></i></div>
<div class="abs rule" style="top:384px"></div>

<div class="abs sample active" style="left:75px">
  <div class="sample-art" role="img" aria-label="Audiobook cover art, dark noir thriller" style="background:radial-gradient(circle at 40% 40%,#6a7070,#1e2526)"></div>
  <h3>Audiobooks</h3>
  <p>Lorem ipsum dolor sit amet,<br>consectetuer adipiscing elit.</p>
  <div class="btn">MORE DETAILS</div>
</div>
<div class="abs sample" style="left:265px">
  <div class="sample-art" role="img" aria-label="Stand-up comedy album art with a boxer" style="background:radial-gradient(circle at 40% 55%,#6a5c4a,#2a2a2c)"></div>
  <h3>Stand-Up Comedy</h3>
  <p>Lorem ipsum dolor sit amet,<br>consectetuer adipiscing elit.</p>
  <div class="btn">MORE DETAILS</div>
</div>
<div class="abs sample" style="left:455px">
  <div class="sample-art" role="img" aria-label="French language course cover, deep blue" style="background:radial-gradient(circle at 50% 40%,#1f6aa8,#0b2f5a)"></div>
  <h3>Language Learning</h3>
  <p>Lorem ipsum dolor sit amet,<br>consectetuer adipiscing elit.</p>
  <div class="btn">MORE DETAILS</div>
</div>
<div class="abs sample" style="left:645px">
  <div class="sample-art" role="img" aria-label="Biography cover with portrait photograph" style="background:radial-gradient(circle at 50% 40%,#c9a78c,#3f5b6c)"></div>
  <h3>Biographies &amp; Memoirs</h3>
  <p>Lorem ipsum dolor sit amet,<br>consectetuer adipiscing elit.</p>
  <div class="btn">MORE DETAILS</div>
</div>

<div class="abs rule" style="top:712px"></div>

<div class="abs feature" style="left:75px;width:229px">
  <div class="feature-art" role="img" aria-label="Illustration of a tablet and a phone showing the service"></div>
  <p>Listen on your <b>Zentro</b>, <b>Slato</b><br>or <b>Andrix</b> device.</p>
</div>
<div class="abs feature" style="left:331px;width:230px">
  <div class="feature-art" role="img" aria-label="Illustration of headphones with a price symbol"></div>
  <p>All you can enjoy for<br>one <b>low</b> monthly <b>price</b>.</p>
</div>
<div class="abs feature" style="left:585px;width:230px">
  <div class="feature-art" role="img" aria-label="Illustration of an alarm clock showing cancel any time"></div>
  <p>No obligation.<br>Cancel any <b>time</b>.</p>
</div>

<div class="abs rule" style="top:996px"></div>

<form class="abs signup">
  <h2>Start Your Free Trial</h2>
  <div class="email"><svg width="16" height="11" viewBox="0 0 16 11"><rect x="0.5" y="0.5" width="15" height="10" fill="none" stroke="#777"/><path d="M0.5 0.5l7.5 6 7.5-6" fill="none" stroke="#777"/></svg>Your Email Adress</div>
  <div class="signup-btn">SIGN UP</div>
  <div class="signup-note">You will get instant &amp; unlimited access to all the material on <em>Olvantra</em> for <span class="g">14 days</span>.<br>There is <strong>no obligation</strong> &amp; you can cancel at <strong>any time</strong>. <span class="soft">Credit Card Not Required for Free Trial.</span></div>
</form>

<div class="abs access">
  <div class="side"><svg width="12" height="15" viewBox="0 0 12 15"><rect x="0" y="6" width="12" height="9" fill="#fff"/><path d="M2.5 6V4a3.5 3.5 0 0 1 7 0v2" stroke="#fff" stroke-width="1.8" fill="none"/></svg></div>
  <span>GET INSTANT ACCESS</span>
</div>
<div class="abs or">OR</div>
<div class="abs social">
  <div class="side"></div>
  <span>SIGN UP USING CHATTERLY</span>
</div>

<div class="abs rule" style="top:1157px"></div>
<footer>
  <div class="abs copyright">© 2014 <strong>Olvantra LLC</strong> - All Rights Reserved</div>
  <div class="abs footer-links">About | Help | Contact Us | Member Login | Privacy Policy | Terms of Service</div>
</footer>

</body>
</html>
```